Stem Cell Facial

B0 Paper Size Poster for the Window. We are a high end Beauty Salon / Day Spa in Sydney NSW Australia.
Must be Organic looking but also attract attention. Must be modern, contemporary, clean and bold. Must our Salon Logo (velunara) (attached). The other image attached can be used, but are more of an indication of the desired look and feel. The word doc contains words that must to be used. Image of female face experiencing a beauty treatment could be used.
The Poster should be in Portrait (not Landscape)
Beauty Salon

```html
<!DOCTYPE html>
<html lang="en">
<head>
<meta charset="utf-8">
<title>Velunara Stem Cell Facial Offer</title>
<link href="https://fonts.googleapis.com/css2?family=Arimo:ital,wght@0,400;0,700;1,400;1,700&display=swap" rel="stylesheet">
<style>
  :root {
    --teal-dark: #1f8c93;
    --teal-mid: #3fb1b5;
    --teal-light: #8fd6d6;
    --skin: #e9d2c4;
    --hair: #1c1a1c;
    --white: #ffffff;
    --ink: #222222;
    --red: #d3282e;
    --pool-stone: #d8cdb6;
    --pool-green: #7f9a73;
    --pool-water: #5f8fa0;
  }
  * { margin: 0; padding: 0; box-sizing: border-box; }
  html, body { width: 849px; height: 1200px; overflow: hidden; background: var(--white); }
  body { font-family: "Arimo", Arial, sans-serif; color: var(--ink); }

  .poster { position: relative; width: 849px; height: 1200px; overflow: hidden; background: var(--white); }

  .hero {
    position: absolute; left: 0; top: 0; width: 849px; height: 570px;
    background:
      radial-gradient(ellipse 250px 320px at 230px 300px, var(--skin) 0%, rgba(233,210,196,0.6) 45%, rgba(233,210,196,0) 75%),
      radial-gradient(ellipse 230px 170px at 210px 70px, var(--hair) 0%, rgba(28,26,28,0) 80%),
      linear-gradient(90deg, #d7e9e8 0%, var(--teal-light) 40%, var(--teal-mid) 62%, var(--teal-dark) 100%);
  }

  .hero-title {
    position: absolute; left: 467px; top: 52px; width: 380px;
    color: var(--white); font-weight: 700; font-size: 56px; line-height: 81px;
    letter-spacing: -0.5px; white-space: nowrap;
  }
  .hero-title span { display: block; }

  .hero-sub {
    position: absolute; left: 470px; top: 492px; width: 370px;
    color: var(--white); font-style: italic; font-size: 29px; line-height: 44px;
    white-space: nowrap;
  }
  .hero-sub span { display: block; }

  .scene {
    position: absolute; left: 0; top: 760px; width: 849px; height: 440px;
    background:
      linear-gradient(180deg, var(--white) 0%, rgba(255,255,255,0.7) 12%, rgba(255,255,255,0) 35%),
      linear-gradient(180deg, #e6e0d0 15%, var(--pool-stone) 45%, var(--pool-green) 72%, var(--pool-water) 100%);
  }

  .offer {
    position: absolute; left: 0; top: 574px; width: 849px; text-align: center;
    font-weight: 700; font-size: 34px; line-height: 52px; color: var(--ink);
    letter-spacing: -0.5px; white-space: nowrap;
  }
  .offer .price { color: var(--red); font-size: 48px; }

  .bonus {
    position: absolute; left: 0; top: 637px; width: 849px; text-align: center;
    font-style: italic; font-size: 21px; color: var(--ink); white-space: nowrap;
  }
  .bonus .worth { color: var(--red); font-weight: 700; }
  .bonus sup { font-size: 14px; color: var(--red); }

  .brand {
    position: absolute; left: 0; top: 698px; width: 849px; text-align: center;
  }
  .brand-name {
    display: block; color: var(--red); font-weight: 700; font-size: 56px; line-height: 60px;
    letter-spacing: 1px;
  }
  .brand-tag {
    display: block; color: var(--ink); font-weight: 700; font-size: 19px;
    letter-spacing: 10px; margin-top: 0;
  }

  .phone {
    position: absolute; left: 0; top: 792px; width: 849px; text-align: center;
    font-weight: 700; font-size: 30px; color: var(--ink);
  }
  .terms {
    position: absolute; right: 22px; top: 795px;
    font-size: 13px; color: var(--ink);
  }
</style>
</head>
<body>
  <main class="poster">
    <div class="hero" role="img" aria-label="Photo of a woman with short dark hair resting her face on her hands against a teal background"></div>
    <h1 class="hero-title"><span>Anti Ageing</span><span>Facial</span><span>Rejuvenation</span><span>Special</span><span>Offer</span></h1>
    <p class="hero-sub"><span>Experience The Power Of</span><span>Plant Stem Cells</span></p>

    <div class="scene" role="img" aria-label="Photo of a woman relaxing in a spa pool with a leafy headpiece, stone arches and palms behind"></div>

    <p class="offer">2 Stem Cell Facials for <span class="price">$249</span> - Save Over <span class="price">$50</span></p>
    <p class="bonus">Bonus Free Stem Cell Crème Worth <span class="worth">$89.95</span><sup>*</sup></p>

    <div class="brand">
      <span class="brand-name">velunara</span>
      <span class="brand-tag">salon &amp; spa</span>
    </div>

    <p class="phone">9318 5046</p>
    <p class="terms">*While stocks last.</p>
  </main>
</body>
</html>
```